arts & crafts

I collect old plates & make them into serving plates for cakes, afternoon teas, special occasions, weddings, parties, bridal showers. cake competitions, displays in bakeries.

Contact Information for Business Card

Tulips Turn Gold
Giving the vintage a fresh start
Ph 0417283956
info@ tulipsturngold.com.au
www.tulipsturngold.com.au
pagebook
Craftlo

```html
<!DOCTYPE html>
<html lang="en">
<head>
<meta charset="utf-8">
<title>Tulips Turn Gold – Business Card</title>
<link rel="stylesheet" href="https://fonts.googleapis.com/css2?family=Sorts+Mill+Goudy&family=Arimo:wght@400&display=swap">
<style>
  :root {
    --backdrop: #9c9c9c;
    --card-purple-deep: #35316b;
    --card-purple: #46428a;
    --card-purple-light: #55529a;
    --band-white: #ffffff;
    --tagline: #6a66a8;
    --ink-white: #ffffff;
    --label-lilac: #c9c7e8;
  }
  html, body {
    margin: 0;
    width: 1200px;
    height: 857px;
    overflow: hidden;
    background: var(--backdrop);
  }
  .card {
    position: absolute;
    left: 100px;
    top: 143px;
    width: 1000px;
    height: 571px;
    overflow: hidden;
    box-shadow: 0 6px 18px rgba(0,0,0,0.25);
  }
  .card__panel {
    position: absolute;
    inset: 0 0 168px 0;
    background: linear-gradient(100deg, var(--card-purple-deep) 0%, var(--card-purple) 55%, var(--card-purple-light) 100%);
  }
  .card__floral {
    position: absolute;
    left: 0;
    top: 60px;
    width: 360px;
    height: 343px;
    background: radial-gradient(ellipse at 40% 60%, rgba(44,40,96,0.75) 0%, rgba(44,40,96,0.35) 45%, rgba(44,40,96,0) 75%);
  }
  .card__title {
    position: absolute;
    left: 120px;
    top: 36px;
    margin: 0;
    font-family: "Sorts Mill Goudy", serif;
    font-weight: 400;
    font-size: 70px;
    line-height: 1;
    color: var(--ink-white);
    white-space: nowrap;
  }
  .card__name {
    position: absolute;
    left: 535px;
    top: 174px;
    margin: 0;
    font-family: "Arimo", sans-serif;
    font-size: 20px;
    letter-spacing: 12px;
    color: var(--ink-white);
    white-space: nowrap;
  }
  .contact {
    position: absolute;
    left: 469px;
    top: 262px;
    margin: 0;
    padding: 0;
    list-style: none;
    font-family: "Arimo", sans-serif;
    font-size: 19px;
    line-height: 28px;
    white-space: nowrap;
  }
  .contact__label { color: var(--label-lilac); margin-right: 4px; }
  .contact__value { color: var(--ink-white); }
  .card__band {
    position: absolute;
    left: 0;
    right: 0;
    bottom: 0;
    height: 168px;
    background: var(--band-white);
    display: flex;
    align-items: center;
    justify-content: center;
  }
  .tagline {
    margin: 0;
    font-family: "Sorts Mill Goudy", serif;
    font-weight: 400;
    font-size: 52px;
    color: var(--tagline);
    white-space: nowrap;
  }
  .tagline__accent {
    font-size: 64px;
    font-weight: 700;
  }
</style>
</head>
<body>
  <section class="card" aria-label="Tulips Turn Gold business card">
    <div class="card__panel"></div>
    <div class="card__floral" role="img" aria-label="Faded blue flowers with scattered water droplets"></div>
    <h1 class="card__title">Tulips Turn Gold</h1>
    <p class="card__name">YOUR NAME ?</p>
    <ul class="contact">
      <li><span class="contact__label">email</span><span class="contact__value">info@tulipsturngold.com.au</span></li>
      <li><span class="contact__label">website</span><span class="contact__value">www.tulipsturngold.com.au</span></li>
      <li><span class="contact__label">pagebook</span></li>
      <li><span class="contact__label">phone</span><span class="contact__value">0417283956</span></li>
    </ul>
    <div class="card__band">
      <p class="tagline">Giving the <span class="tagline__accent">vintage</span> a <span class="tagline__accent">fresh</span> start</p>
    </div>
  </section>
</body>
</html>
```